Business card design needed for Automotive Reconditioning business

I have a logo design i just cant decide on the best color or layout for the business card, I will upload all the files so you can see all colors schemes we are considering. I have other file formats if needed let me know.

Target Market(s)

automotive dealerships

Contact Information for Business Card

HERE are the Descriptions and info needed on the card:
Interior Repair: Leather carpet burns panels dash Deoderize
Dealer products and Vin Verify
( spot for name and cell number) My name is Dorian Pelk phone 951 430-2158 Title COO www.BrolvexMotor.com

Font styles to use
Sans Serif
Other font styles liked:
• what ever you think looks best

Requirements
Must have
• Must be able to change the name and phone for employees

```html
<!DOCTYPE html>
<html lang="en">
<head>
<meta charset="utf-8">
<title>Brolvex Motor Reconditioning Corp. – Business Card</title>
<link href="https://fonts.googleapis.com/css2?family=Montserrat:wght@500;700;800&family=Open+Sans:wght@400;600&display=swap" rel="stylesheet">
<style>
  :root {
    --canvas: #e9e6e1;
    --card-white: #f4f4f4;
    --carbon: #2b2c2e;
    --brand-blue: #1f7fc9;
    --brand-cyan: #1fa6df;
    --brand-red: #e0302a;
    --text-light: #ffffff;
    --text-soft: #4fb3e8;
    --text-dark: #222222;
  }
  * { margin: 0; padding: 0; box-sizing: border-box; }
  html, body { width: 1200px; height: 780px; overflow: hidden; background: var(--canvas); }
  .canvas { position: relative; width: 1200px; height: 780px; }
  .card {
    position: absolute; top: 230px; width: 560px; height: 320px;
    border-radius: 16px; overflow: hidden; background: var(--card-white);
    box-shadow: 0 10px 24px rgba(0,0,0,.18);
  }
  .card--front { left: 25px; }
  .card--back { left: 615px; }
  .card svg.card-shapes { position: absolute; inset: 0; width: 560px; height: 320px; }

  .brand-mark { position: absolute; display: flex; align-items: center; gap: 10px; }
  .brand-mark__dot { width: 22px; height: 22px; border-radius: 50%; background: var(--brand-blue); flex: none; }
  .brand-mark__name {
    font-family: "Montserrat", sans-serif; font-weight: 800; color: var(--brand-red);
    text-transform: uppercase; line-height: 1.08; letter-spacing: .5px; white-space: nowrap;
  }
  .card--front .brand-mark { left: 28px; top: 62px; }
  .card--front .brand-mark__name { font-size: 22px; }
  .card--back .brand-mark { left: 232px; top: 66px; }
  .card--back .brand-mark__name { font-size: 26px; }

  .contact { position: absolute; left: 292px; top: 168px; display: flex; align-items: center; gap: 12px; }
  .contact__person { text-align: right; }
  .contact__name { font-family: "Montserrat", sans-serif; font-weight: 700; font-size: 14px; color: var(--text-light); text-transform: uppercase; white-space: nowrap; }
  .contact__title { font-family: "Open Sans", sans-serif; font-size: 11.5px; color: var(--text-soft); white-space: nowrap; }
  .contact__divider { width: 1px; height: 44px; background: #9a9ca0; }
  .contact__phones { list-style: none; }
  .contact__phone { display: flex; align-items: center; gap: 6px; font-family: "Open Sans", sans-serif; font-weight: 600; font-size: 13px; color: var(--text-light); line-height: 1.6; white-space: nowrap; }
  .contact__icon { width: 15px; height: 15px; border-radius: 3px; background: var(--brand-cyan); display: flex; align-items: center; justify-content: center; }

  .services {
    position: absolute; left: 16px; right: 16px; bottom: 10px;
    font-family: "Open Sans", sans-serif; font-weight: 600; font-size: 11px;
    color: var(--text-light); text-align: right; letter-spacing: .2px; white-space: nowrap;
  }
  .website {
    position: absolute; left: 312px; top: 212px;
    font-family: "Open Sans", sans-serif; font-size: 12px; letter-spacing: 3px; color: var(--text-dark); white-space: nowrap;
  }
  .website__domain { color: var(--brand-red); }
</style>
</head>
<body>
<main class="canvas">

  <section class="card card--front" aria-label="Card front">
    <svg class="card-shapes" viewBox="0 0 560 320" aria-hidden="true">
      <rect class="carbon-field" width="560" height="320" fill="var(--carbon)"/>
      <path class="blue-swoosh" d="M330 0 L362 0 C335 160 215 262 0 296 L0 284 Z" fill="var(--brand-blue)"/>
      <path class="white-field" d="M0 0 L330 0 C305 150 190 245 0 284 Z" fill="var(--card-white)"/>
      <path class="red-rule" d="M316 0 C292 146 180 238 0 274" fill="none" stroke="var(--brand-red)" stroke-width="2.5"/>
      <rect class="service-band" x="0" y="288" width="560" height="32" fill="var(--brand-cyan)"/>
      <line x1="0" y1="287" x2="560" y2="287" stroke="var(--brand-red)" stroke-width="2.5"/>
    </svg>

    <div class="brand-mark">
      <span class="brand-mark__dot"></span>
      <span class="brand-mark__name">Brolvex Motor<br>Reconditioning<br>Corp.</span>
    </div>

    <div class="contact">
      <div class="contact__person">
        <p class="contact__name">Dorian Pelk</p>
        <p class="contact__title">Interior Specialist</p>
      </div>
      <span class="contact__divider"></span>
      <ul class="contact__phones">
        <li class="contact__phone">
          <span class="contact__icon">
            <svg width="9" height="11" viewBox="0 0 9 11"><rect x="1" y="0.5" width="7" height="10" rx="1.5" fill="none" stroke="#fff" stroke-width="1.2"/><circle cx="4.5" cy="8.5" r=".8" fill="#fff"/></svg>
          </span>951 430-2158
        </li>
        <li class="contact__phone">
          <span class="contact__icon">
            <svg width="11" height="11" viewBox="0 0 11 11"><path d="M2 1 L4 1 L4.8 3.4 L3.6 4.4 C4.2 5.8 5.2 6.8 6.6 7.4 L7.6 6.2 L10 7 L10 9 C10 9.6 9.6 10 9 10 C4.6 10 1 6.4 1 2 C1 1.4 1.4 1 2 1 Z" fill="#fff"/></svg>
          </span>951 430-2197
        </li>
      </ul>
    </div>

    <p class="services">Leather | Burns | Panels | Deodorize | Touch-Up | Dealer Products | Vin Verify</p>
  </section>

  <section class="card card--back" aria-label="Card back">
    <svg class="card-shapes" viewBox="0 0 560 320" aria-hidden="true">
      <path class="carbon-field" d="M0 0 L70 0 C120 150 260 270 520 320 L0 320 Z" fill="var(--carbon)"/>
      <path class="blue-swoosh" d="M70 0 C120 150 260 270 520 320 L560 320 C300 280 150 160 100 0 Z" fill="var(--brand-blue)"/>
      <path class="white-field" d="M100 0 C150 160 300 280 560 320 L560 0 Z" fill="var(--card-white)"/>
      <path class="red-rule" d="M112 0 C162 158 312 276 560 312" fill="none" stroke="var(--brand-red)" stroke-width="2.5"/>
    </svg>

    <div class="brand-mark">
      <span class="brand-mark__dot"></span>
      <span class="brand-mark__name">Brolvex Motor<br>Reconditioning<br>Corp.</span>
    </div>

    <p class="website">www.<span class="website__domain">BrolvexMotor</span>.com</p>
  </section>

</main>
</body>
</html>
```